App User Interface Design for Bible App

The task is to redesign an existing windows phone and windows 10 app to make it purely universal app which will be launched on iOS and Android platforms also.

This is one of the top 5 bible apps in the windows store and i want to make it the best in all platform. App screenshots are on the ScrollHaven.com site.

UI will be seamless across Windows, iOS and Android.

As part of the design process i will love to get a new app logo and app icon.

Current app details can be found at scrollhaven.com

I need the following screens in the design concept you submit.
1. Home Screen
2. Reading Screen with Single Bible Version
3. Parallel Reading Screen with Two Bible Versions
4. Bible Books Selection/Chapter/Verse Selection
5. Bible Reading Plan Listing
6. Bible Reading Detail for a given day
7. Bible Versions Listing

Target Market(s)

Worldwide

Industry/Entity Type

Android

Font styles to use
Sans Serif

Requirements
Must have
• Some sort visual that they are going to use a Bible App.
• The design must be able to work as a cross platform app on Windows, iOS and Android.
• Once the app opens it should have some place to show verse of the day. We will be removing the Random verse feature.
• Text should be very easy to read and they should be able to change font settings easily.
• Easy way to access the following:
• Bible Books, Chapters and Verses
• Versions (They are available in multiple languages)
• Should be able to access last read new testament verse
• Should be able to access last read old testament verse
• Should be able to access last read parallel versions verse
• Daily Reading Plans
• Notes
• Bookmarks
• Highlights
• Backup and Restore
• Donate option
Nice to have
• Easier way for users to change bible versions as they are reading. In current app its a little confusing.
• Better way to list, add, view notes
• Better Reading mode
• Better Parallel Reading mode
Should not have
• Should not be cloned or copied from other bible apps in the market place.
• Should not be a generic iOS or Android based design. Remember, I want to make this a cross platform application on iOS, Windows and Android.

```html
<!DOCTYPE html>
<html lang="en">
<head>
<meta charset="utf-8">
<title>Bible App – Screens</title>
<link href="https://fonts.googleapis.com/css2?family=Open+Sans:wght@400;600;700&family=Tinos:wght@400;700&display=swap" rel="stylesheet">
<style>
:root{
  --stage:#57534c;
  --gold:#d9a42b;
  --paper:#ffffff;
  --mist:#ececec;
  --line:#dcdcdc;
  --ink:#2b2b2b;
  --muted:#8a8a8a;
  --ui:"Open Sans", Arial, sans-serif;
  --read:"Tinos", "Times New Roman", serif;
}
*{box-sizing:border-box;margin:0;padding:0}
html,body{width:699px;height:1200px;overflow:hidden;background:var(--stage)}
.stage{position:relative;width:699px;height:1200px}
.screen{position:absolute;width:322px;height:566px;background:var(--mist);overflow:hidden;font-family:var(--ui);color:var(--ink)}
.s-home{left:20px;top:18px}
.s-books{left:358px;top:18px}
.s-chapters{left:20px;top:614px}
.s-reader{left:358px;top:614px;background:var(--paper)}

.status{height:18px;background:var(--paper);display:flex;align-items:center;justify-content:space-between;padding:0 6px;font-size:9px;font-weight:600;color:#222}
.status .battery{display:inline-block;width:16px;height:7px;border:1px solid #222;border-radius:1px;vertical-align:middle;margin-left:3px;background:#222}
.appbar{height:40px;background:var(--gold);display:flex;align-items:center;justify-content:center;position:relative;color:#fff;font-size:15px;font-weight:600}
.appbar .lead{position:absolute;left:10px;top:9px}
.appbar .trail{position:absolute;right:12px;font-size:13px}

.card{background:var(--paper);margin:8px 8px 0;border-radius:2px}
.votd{padding:12px 12px 12px;text-align:center}
.label{font-size:10px;font-weight:600;color:var(--muted);letter-spacing:.3px}
.date{font-size:11px;font-weight:600;color:var(--gold);margin-top:2px}
.verse{font-family:var(--read);font-size:14.5px;line-height:1.4;color:var(--ink);text-align:justify;margin-top:10px}
.ref{font-size:11px;color:var(--gold);text-align:right;margin-top:8px}
.row{display:flex;align-items:center;gap:8px;padding:14px 12px;font-size:11px;font-weight:600;color:#555;letter-spacing:.2px}
.row svg{flex:none}
.tabs{display:flex;margin:0 10px;border:1px solid var(--gold)}
.tabs span{flex:1;text-align:center;font-size:8.5px;font-weight:600;padding:6px 0;color:var(--gold);background:var(--paper)}
.tabs span.on{background:var(--gold);color:#fff}
.lastread{padding:12px 12px 14px}
.lastread .verse{margin-top:0}

.books-tabs{display:flex;margin:10px 12px;border:1px solid var(--gold)}
.books-tabs span{flex:1;text-align:center;font-size:11px;font-weight:600;padding:6px 0;color:var(--gold);background:var(--paper)}
.books-tabs span.on{background:var(--gold);color:#fff}
.booklist{list-style:none;background:var(--paper)}
.booklist li{display:flex;align-items:center;height:51px;padding:0 12px;border-bottom:1px solid var(--line)}
.booklist .name{flex:1;margin-left:10px;font-size:13px;font-weight:700;color:#333}
.booklist .count{font-size:11px;color:var(--muted)}
.booklist .count b{font-weight:400;color:#999;margin-left:6px}

.pager{height:34px;background:var(--paper);display:flex;align-items:center;justify-content:space-between;padding:0 14px;border-bottom:1px solid var(--line);color:var(--gold);font-size:13px;font-weight:700}
.grid{display:grid;grid-template-columns:repeat(5,52px);gap:16px 9px;padding:18px 13px}
.grid span{height:52px;background:var(--paper);border:1px solid var(--line);display:flex;align-items:center;justify-content:center;font-size:14px;color:#444}
.grid span.on{background:var(--gold);border-color:var(--gold);color:#fff}

.reading{padding:12px 12px;font-family:var(--read);font-size:14.5px;line-height:1.38;color:var(--ink)}
.reading h2{font-size:15px;font-weight:700;text-align:center;margin-bottom:10px}
.reading p{text-align:justify;text-indent:10px;margin-bottom:6px}
.reading p b{margin-right:3px}
</style>
</head>
<body>
<main class="stage">

  <section class="screen s-home">
    <div class="status"><span>●●●●○ Carrier</span><span>4:21 PM</span><span>100%<i class="battery"></i></span></div>
    <header class="appbar">
      <svg class="lead" width="22" height="22" viewBox="0 0 22 22"><circle cx="11" cy="11" r="10" fill="none" stroke="#fff" stroke-width="1.5"/><path d="M6.5 7.5h9M6.5 11h9M6.5 14.5h9" stroke="#fff" stroke-width="1.5"/></svg>
      Home
    </header>
    <article class="card votd">
      <div class="label">VERSE OF THE DAY</div>
      <div class="date">22 OCT 2015</div>
      <p class="verse">But seek first the kingdom of God and His righteousness, and all these things shall be added to you.</p>
      <div class="ref">Matthew 6:33, SHV</div>
    </article>
    <div class="card row">
      <svg width="14" height="16" viewBox="0 0 14 16"><rect x="1" y="1" width="12" height="14" rx="1" fill="none" stroke="#777" stroke-width="1.4"/><path d="M7 4v7M4.5 6.5h5" stroke="#777" stroke-width="1.4"/></svg>
      BIBLE (SELECT A BOOK)
    </div>
    <div class="card">
      <div class="row">
        <svg width="16" height="14" viewBox="0 0 16 14"><path d="M1 2h5.5c1 0 1.5.6 1.5 1.5V13c0-.8-.6-1.3-1.5-1.3H1zM15 2H9.5C8.5 2 8 2.6 8 3.5V13c0-.8.6-1.3 1.5-1.3H15z" fill="none" stroke="#777" stroke-width="1.3"/></svg>
        LAST READ VERSES
      </div>
      <div class="tabs"><span>OLD TESTAMENT</span><span class="on">NEW TESTAMENT</span><span>PARALLEL VERSE</span></div>
      <div class="lastread">
        <p class="verse">- the Spirit of truth. The world cannot accept him, because it neither sees him nor knows him. But you know him, for he lives with you and will be in you.</p>
        <div class="ref">John 14:17, SHV</div>
      </div>
    </div>
  </section>

  <section class="screen s-books">
    <div class="status"><span>●●●●○ Carrier</span><span>4:21 PM</span><span>100%<i class="battery"></i></span></div>
    <header class="appbar">
      <svg class="lead" width="22" height="22" viewBox="0 0 22 22"><circle cx="11" cy="11" r="10" fill="none" stroke="#fff" stroke-width="1.5"/><path d="M12.5 6.5L8 11l4.5 4.5M8 11h7" fill="none" stroke="#fff" stroke-width="1.5"/></svg>
      Select a Book
    </header>
    <div class="books-tabs"><span class="on">OLD TESTAMENT</span><span>NEW TESTAMENT</span></div>
    <ul class="booklist">
      <li><svg width="12" height="14" viewBox="0 0 12 14"><rect width="12" height="14" rx="1" fill="#8a8a8a"/><path d="M6 3v7M3.5 5.5h5" stroke="#fff" stroke-width="1.3"/></svg><span class="name">MATTHEW</span><span class="count">28 Chapters<b>›</b></span></li>
      <li><svg width="12" height="14" viewBox="0 0 12 14"><rect width="12" height="14" rx="1" fill="#8a8a8a"/><path d="M6 3v7M3.5 5.5h5" stroke="#fff" stroke-width="1.3"/></svg><span class="name">MARK</span><span class="count">16 Chapters<b>›</b></span></li>
      <li><svg width="12" height="14" viewBox="0 0 12 14"><rect width="12" height="14" rx="1" fill="#8a8a8a"/><path d="M6 3v7M3.5 5.5h5" stroke="#fff" stroke-width="1.3"/></svg><span class="name">LUKE</span><span class="count">24 Chapters<b>›</b></span></li>
      <li><svg width="12" height="14" viewBox="0 0 12 14"><rect width="12" height="14" rx="1" fill="#8a8a8a"/><path d="M6 3v7M3.5 5.5h5" stroke="#fff" stroke-width="1.3"/></svg><span class="name">JOHN</span><span class="count">21 Chapters<b>›</b></span></li>
      <li><svg width="12" height="14" viewBox="0 0 12 14"><rect width="12" height="14" rx="1" fill="#8a8a8a"/><path d="M6 3v7M3.5 5.5h5" stroke="#fff" stroke-width="1.3"/></svg><span class="name">ACTS</span><span class="count">28 Chapters<b>›</b></span></li>
      <li><svg width="12" height="14" viewBox="0 0 12 14"><rect width="12" height="14" rx="1" fill="#8a8a8a"/><path d="M6 3v7M3.5 5.5h5" stroke="#fff" stroke-width="1.3"/></svg><span class="name">ROMANS</span><span class="count">16 Chapters<b>›</b></span></li>
      <li><svg width="12" height="14" viewBox="0 0 12 14"><rect width="12" height="14" rx="1" fill="#8a8a8a"/><path d="M6 3v7M3.5 5.5h5" stroke="#fff" stroke-width="1.3"/></svg><span class="name">1 CORINTHIANS</span><span class="count">16 Chapters<b>›</b></span></li>
      <li><svg width="12" height="14" viewBox="0 0 12 14"><rect width="12" height="14" rx="1" fill="#8a8a8a"/><path d="M6 3v7M3.5 5.5h5" stroke="#fff" stroke-width="1.3"/></svg><span class="name">2 CORINTHIANS</span><span class="count">13 Chapters<b>›</b></span></li>
      <li><svg width="12" height="14" viewBox="0 0 12 14"><rect width="12" height="14" rx="1" fill="#8a8a8a"/><path d="M6 3v7M3.5 5.5h5" stroke="#fff" stroke-width="1.3"/></svg><span class="name">GALATIANS</span><span class="count">6 Chapters<b>›</b></span></li>
    </ul>
  </section>

  <section class="screen s-chapters">
    <div class="status"><span>●●●●○ Carrier</span><span>4:21 PM</span><span>100%<i class="battery"></i></span></div>
    <header class="appbar">
      <svg class="lead" width="22" height="22" viewBox="0 0 22 22"><circle cx="11" cy="11" r="10" fill="none" stroke="#fff" stroke-width="1.5"/><path d="M12.5 6.5L8 11l4.5 4.5M8 11h7" fill="none" stroke="#fff" stroke-width="1.5"/></svg>
      Select a Chapter
    </header>
    <div class="pager"><span>‹</span><span>JOHN</span><span>›</span></div>
    <div class="grid">
      <span>1</span><span>2</span><span>3</span><span>4</span><span>5</span>
      <span>6</span><span>7</span><span>8</span><span>9</span><span>10</span>
      <span>11</span><span>12</span><span>13</span><span class="on">14</span><span>15</span>
      <span>16</span><span>17</span><span>18</span><span>19</span><span>20</span>
      <span>21</span>
    </div>
  </section>

  <section class="screen s-reader">
    <div class="status"><span>●●●●○ Carrier</span><span>4:21 PM</span><span>100%<i class="battery"></i></span></div>
    <header class="appbar">
      <svg class="lead" width="22" height="22" viewBox="0 0 22 22"><circle cx="11" cy="11" r="10" fill="none" stroke="#fff" stroke-width="1.5"/><path d="M12.5 6.5L8 11l4.5 4.5M8 11h7" fill="none" stroke="#fff" stroke-width="1.5"/></svg>
      John
      <span class="trail">SHV</span>
    </header>
    <div class="pager"><span>‹</span><span>Chapter 14</span><span>›</span></div>
    <div class="reading">
      <h2>The Way, the Truth, and the Life</h2>
      <p><b>1</b>“Let not your heart be troubled; you believe in God, believe also in Me.</p>
      <p><b>2</b>In My Father’s house are many mansions; if it were not so, I would have told you. I go to prepare a place for you.</p>
      <p><b>3</b>And if I go and prepare a place for you, I will come again and receive you to Myself; that where I am, there you may be also.</p>
      <p><b>4</b>And where I go you know, and the way you know.”</p>
      <p><b>5</b>Thomas said to Him, “Lord, we do not know where You are going, and how can we know the way?”</p>
      <p><b>6</b>Jesus said to him, “I am the way, the truth, and the life. No one comes to the Father except through Me.</p>
      <p><b>7</b>“If you had known Me, you would have known My Father also; and from now on you know Him and have seen Him.”</p>
      <p><b>8</b>Philip said to Him, “Lord, show us the Father, and it is sufficient for us.”</p>
    </div>
  </section>

</main>
</body>
</html>
```